Social Media Graphics - Copperfield Loop

Create 6-7 individual social media graphics (square size) to encourage folks to join our online course, using either of the text below (only one set of text per graphic:

The Lantern Ridge Method
How to Create a 7-Figure Business From Scratch
Sign Up Today!

Or

The Lantern Ridge Method
Fast-track Your Way to a Multi-Million Business!
Sign Up Today!

For the color scheme of the graphics, use 1 or 2 colors in the color palette attached; or use any colors that look nice with their outfits; AVOID using red, white and blue altogether because it will look like an Independence Day (4th of July) graphic and we don’t want that; make sure the graphics appeal to both men and women

Make sure each graphic contains 1 of the 2 pics attached; and make sure one of the graphics is all TEXT only.

Target Market(s)

men and women looking to make more money

Industry/Entity Type

entrepreneurship

Requirements
Must have
• see the text document attached
Nice to have
• We are open to a nice color design; the color palette colors are not required, especially we don't want red, white and blue used together
Should not have
• AVOID using red, white and blue altogether because it will look like an Independence Day (4th of July) graphic and we dont want that

```html
<!DOCTYPE html>
<html lang="en">
<head>
<meta charset="utf-8">
<title>The Lantern Ridge Method – Social Graphics</title>
<link rel="stylesheet" href="https://fonts.googleapis.com/css2?family=Anton&family=Oswald:wght@600;700&family=Poppins:wght@500;600&display=swap">
<style>
  :root{
    --canvas:#898989;
    --amber:#efac04;
    --cream:#f8eacb;
    --ink:#111111;
    --text-dark:#2b2b2b;
    --teal-deep:#0b4f55;
    --teal-bright:#08d6c9;
    --butter:#fbeaa0;
    --butter-light:#fdf3c6;
    --yellow:#f6e100;
    --pink:#fbbccd;
    --pink-bar:#f799b3;
    --maroon:#7d0a2a;
    --red:#cf1323;
    --bar-grey:#4a4a4a;
    --green:#0a8a14;
    --green-light:#b4fba8;
    --green-pale:#e4f9e5;
    --white:#ffffff;
    --photo-warm:#c98a6a;
    --photo-dark:#2d2320;
  }
  *{margin:0;padding:0;box-sizing:border-box}
  html,body{width:1200px;height:729px;overflow:hidden;background:var(--canvas)}
  .board{position:relative;width:1200px;height:729px}
  .tile{position:absolute;width:278px;height:278px;overflow:hidden}
  .col-1{left:149px}.col-2{left:461px}.col-3{left:773px}
  .row-1{top:69px}.row-2{top:382px}
  .abs{position:absolute}
  .display{font-family:"Anton",sans-serif;font-weight:400;line-height:1}
  .cond{font-family:"Oswald",sans-serif;font-weight:700;line-height:1}
  .body{font-family:"Poppins",sans-serif;font-weight:500;line-height:1.08}
  .photo{position:absolute;background:linear-gradient(160deg,var(--photo-warm),var(--photo-dark))}

  /* Tile 1 – amber */
  .amber{background:var(--cream)}
  .amber .title{left:0;right:0;top:24px;text-align:center;font-size:22px;color:var(--ink)}
  .amber .sub{left:33px;top:79px;font-size:21px;color:var(--text-dark)}
  .amber .photo{left:0;top:155px;width:145px;height:123px;border-radius:60px 60px 0 0}
  .amber .badge{left:167px;top:165px;width:90px;height:90px;border-radius:50%;background:var(--amber);border:3px solid var(--amber);box-shadow:inset 0 0 0 4px var(--amber),inset 0 0 0 5px var(--cream)}
  .amber .badge span{position:absolute;inset:0;display:flex;align-items:center;justify-content:center;text-align:center;transform:rotate(28deg);font-family:"Poppins",sans-serif;font-weight:600;font-size:12px;line-height:1.05;color:var(--ink)}

  /* Tile 2 – teal */
  .teal .photo{inset:0;background:linear-gradient(120deg,var(--teal-deep) 0%,#0f8e8c 50%,var(--teal-bright) 100%)}
  .teal .title{left:0;right:0;top:80px;text-align:center;font-size:23px;color:var(--white)}
  .teal .sub{left:0;right:0;top:125px;text-align:center;font-size:19px;line-height:1.35;color:var(--white)}
  .teal .cta{left:52px;top:207px;width:174px;height:47px;border:2px solid var(--white);border-radius:12px;display:flex;align-items:center;justify-content:center;font-size:19px;color:var(--white)}

  /* Tile 3 – butter */
  .butter{background:radial-gradient(circle at 90% 10%,var(--butter-light),var(--butter) 70%)}
  .butter .title{left:0;right:0;top:18px;text-align:center;font-size:38px;line-height:1.12;color:var(--ink)}
  .butter .sub{left:0;right:0;top:122px;text-align:center;font-size:19px;line-height:1.3;color:var(--text-dark)}
  .butter .bar{left:0;right:0;bottom:0;height:41px;background:var(--ink);display:flex;align-items:center;justify-content:center;font-size:22px;color:var(--yellow)}

  /* Tile 4 – pink / maroon */
  .rose{background:var(--pink)}
  .rose .photo{left:0;top:90px;width:145px;height:188px;border-radius:60px 60px 0 0}
  .rose .title{right:12px;top:22px;text-align:right;font-size:21px;line-height:1.1;color:var(--white);white-space:nowrap}
  .rose .sub{right:12px;top:84px;text-align:right;font-size:20px;line-height:1.06;color:var(--pink)}
  .rose .badge{left:93px;top:143px;width:92px;height:92px;border-radius:50%;background:var(--red);display:flex;align-items:center;justify-content:center;text-align:center;font-family:"Poppins",sans-serif;font-weight:500;font-size:13px;line-height:1.2;color:var(--white)}

  /* Tile 5 – green wave */
  .meadow{background:var(--green)}
  .meadow .title{left:16px;top:17px;font-size:23px;color:var(--white)}
  .meadow .sub{left:16px;top:88px;font-size:17px;line-height:1.6;font-weight:600;color:#14500f}
  .meadow .photo{left:142px;top:53px;width:178px;height:178px;border-radius:50%;border:2px solid var(--white)}
  .meadow .cta{left:16px;top:236px;font-size:25px;color:var(--white)}

  /* Tile 6 – text only */
  .textonly{background:var(--white)}
  .textonly .head{left:0;right:0;top:0;height:52px;background:var(--green);display:flex;align-items:center;justify-content:center;font-size:22px;color:var(--white)}
  .textonly .head::before,.textonly .head::after{content:"";position:absolute;left:0;right:0;border-top:1px dashed var(--green-pale)}
  .textonly .head::before{top:5px}.textonly .head::after{bottom:5px}
  .textonly .msg{left:0;right:0;top:72px;text-align:center;font-size:29px;line-height:1.25;font-weight:600;color:var(--green)}
  .textonly .foot{left:0;right:0;bottom:0;height:50px;background:var(--green);display:flex;align-items:center;justify-content:center;font-size:21px;color:var(--white)}
</style>
</head>
<body>
<main class="board">

  <!-- Amber tile -->
  <section class="tile col-1 row-1 amber">
    <svg class="abs" width="278" height="80" viewBox="0 0 278 80" aria-hidden="true">
      <path d="M0 0H278V73Q200 64 140 64T0 62Z" fill="var(--amber)"/>
      <path d="M0 62Q80 60 140 62T278 67" fill="none" stroke="var(--cream)" stroke-width="1" stroke-dasharray="1 2"/>
    </svg>
    <h2 class="abs display title">THE LANTERN RIDGE METHOD</h2>
    <p class="abs body sub">How to Create a<br>7-Figure Business<br>From Scratch</p>
    <div class="photo" role="img" aria-label="Photo of the two course hosts standing with arms crossed"></div>
    <div class="abs badge"><span>SIGN UP<br>TODAY!</span></div>
  </section>

  <!-- Teal tile -->
  <section class="tile col-2 row-1 teal">
    <div class="photo" role="img" aria-label="Teal-tinted photo of the two course hosts in an office"></div>
    <h2 class="abs display title">THE LANTERN RIDGE METHOD</h2>
    <p class="abs body sub">How to Create a 7-Figure<br>Business From Scratch</p>
    <div class="abs cond cta">SIGN UP TODAY!</div>
  </section>

  <!-- Butter tile -->
  <section class="tile col-3 row-1 butter">
    <h2 class="abs display title">The Lantern Ridge<br>Method</h2>
    <p class="abs body sub">How to Create<br>a 7-Figure<br>Business From<br>Scratch</p>
    <div class="abs cond bar">Sign Up Today!</div>
  </section>

  <!-- Rose tile -->
  <section class="tile col-1 row-2 rose">
    <svg class="abs" width="278" height="278" viewBox="0 0 278 278" aria-hidden="true">
      <path d="M135 0H278V278H145Q185 240 150 190Q110 130 128 70Q138 30 135 0Z" fill="var(--maroon)"/>
      <rect x="0" y="6" width="32" height="10" rx="5" fill="var(--pink-bar)"/>
      <rect x="-6" y="22" width="112" height="10" rx="5" fill="var(--bar-grey)"/>
      <rect x="46" y="39" width="60" height="10" rx="5" fill="var(--pink-bar)"/>
      <rect x="173" y="225" width="47" height="11" rx="5.5" fill="var(--pink-bar)"/>
      <rect x="173" y="243" width="115" height="11" rx="5.5" fill="var(--bar-grey)"/>
      <rect x="234" y="261" width="50" height="11" rx="5.5" fill="var(--pink-bar)"/>
    </svg>
    <div class="photo" role="img" aria-label="Photo of the two course hosts standing with arms crossed"></div>
    <h2 class="abs display title">THE LANTERN<br>RIDGE METHOD</h2>
    <p class="abs body sub">How to Create<br>a 7-Figure<br>Business<br>From<br>Scratch</p>
    <div class="abs badge">SIGN UP<br>TODAY!</div>
  </section>

  <!-- Meadow tile -->
  <section class="tile col-2 row-2 meadow">
    <svg class="abs" width="278" height="278" viewBox="0 0 278 278" aria-hidden="true">
      <path d="M0 68Q90 70 170 55T278 62V205Q200 198 120 212T0 205Z" fill="var(--green-light)"/>
    </svg>
    <h2 class="abs cond title">The Lantern Ridge Method</h2>
    <p class="abs body sub">How to Create<br>a 7-Figure<br>Business<br>From Scratch</p>
    <div class="photo" role="img" aria-label="Circular photo of the two course hosts"></div>
    <div class="abs display cta">SIGN UP TODAY!</div>
  </section>

  <!-- Text-only tile -->
  <section class="tile col-3 row-2 textonly">
    <svg class="abs" width="278" height="278" viewBox="0 0 278 278" aria-hidden="true">
      <circle cx="45" cy="95" r="55" fill="var(--green-pale)"/>
      <circle cx="250" cy="215" r="75" fill="var(--green-pale)"/>
    </svg>
    <h2 class="abs cond head">The Lantern Ridge Method</h2>
    <p class="abs body msg">Fast-track Your<br>Way to a<br>Multi-Million<br>Business!</p>
    <div class="abs cond foot">Sign Up Today!</div>
  </section>

</main>
</body>
</html>
```